依頼詳細
サイト内の雰囲気が黒基調なので、遷移後あまり違和感がないもの、かつバナーの時点でCVが上がりそうなデザインを希望します。
Zentroのディスプレイ広告にはガイドラインがあるようで、その点を踏まえて作成をお願い致します。
記載項目
キャッチコピーはお任せ致しますが
これまでに味わったことがない鯛料理を提供しているお店、鯛料理を定義するという理念のもと、営業しています。
ロゴと写真は以下に格納致します。
https://files.kumovault.example/share/8XqTm3LwR7pNc2Vd5HbJ9sKfA4yUeG6o?mode=view
サイズ
• 300 x 250 ( ミディアムレクタングル )
• 250 x 250 ( スクエアポップアップ )
• 200 x 200 ( スクエア )
• 728 x 90 ( リーダーボード )
• 468 x 60 ( フルバナー )
• 160 x 600 ( ワイドスカイスクレイパー )
• 120 x 600 ( スカイスクレイパー )
• 120 x 240 ( バーティカルバナー )
• Zentroのディスプレイ広告のサイズがわからなかった為、全てにチェックしております。
希望イメージ
シンプル 複雑
単色 カラフル
暗い 明るい
日常 高級
遊び心 厳粛
未来的 伝統的
女性的 男性的
希望する色
納品ファイル
補足説明
■ 選んだ理由

とても清潔感あって素敵なバナーと感じた為、選定させて頂きました。

■ 提案者全員のお礼・コメント

この度は、ご提案頂きましてありがとうございました。今後もよろしくお願い致します。

```html
<!DOCTYPE html>
<html lang="ja">
<head>
<meta charset="utf-8">
<title>汐凪 神楽坂 縦型バナー</title>
<link rel="stylesheet" href="https://fonts.googleapis.com/css2?family=Noto+Serif+JP:wght@500;700;900&display=swap">
<style>
  :root {
    --bg: #000000;
    --ink: #f4f2ee;
    --gold-light: #f6e2ae;
    --gold-mid: #d4a64f;
    --gold-deep: #9a6a22;
    --fish-a: #e8a59a;
    --fish-b: #b9624f;
    --tray: #8a6a3a;
    --glass-top: #2a2a2a;
    --wine: #e9dfb8;
    --stamp: #b3261e;
  }
  * { margin: 0; padding: 0; box-sizing: border-box; }
  html, body {
    width: 1200px; height: 4500px; overflow: hidden;
    background: var(--bg);
  }
  .banner {
    position: relative; width: 1200px; height: 4500px;
    background: var(--bg);
    font-family: "Noto Serif JP", serif;
    color: var(--ink);
  }
  .copy {
    position: absolute;
    writing-mode: vertical-rl;
    text-orientation: upright;
    line-height: 1;
    white-space: nowrap;
  }
  .copy-lead {
    top: 56px; left: 1018px;
    font-size: 122px; font-weight: 700;
    letter-spacing: 6px;
  }
  .copy-main {
    top: 230px; left: 670px;
    font-size: 228px; font-weight: 900;
    letter-spacing: 10px;
    background: linear-gradient(180deg, var(--gold-light) 0%, var(--gold-mid) 40%, var(--gold-deep) 70%, var(--gold-light) 100%);
    -webkit-background-clip: text; background-clip: text;
    color: transparent;
  }
  .copy-sub {
    top: 120px; left: 168px;
    font-size: 132px; font-weight: 700;
    letter-spacing: 8px;
  }
  .photo-fish {
    position: absolute; left: 40px; top: 2500px;
    width: 1140px; height: 680px;
    border-radius: 24px;
    background:
      radial-gradient(ellipse 55% 35% at 45% 40%, var(--fish-a), transparent 70%),
      radial-gradient(ellipse 50% 30% at 50% 65%, var(--fish-b), transparent 75%),
      linear-gradient(170deg, #1a1a14 0%, var(--tray) 60%, #3d2e17 100%);
  }
  .photo-wine {
    position: absolute; left: 60px; top: 3190px;
    width: 440px; height: 1260px;
    border-radius: 200px 200px 40px 40px;
    background: linear-gradient(180deg, var(--glass-top) 0%, #3a3a36 30%, var(--wine) 45%, #a79c78 62%, #2a2a28 70%, #1a1a1a 100%);
  }
  .brand {
    position: absolute; left: 640px; top: 3700px;
    display: flex; align-items: center; gap: 40px;
  }
  .brand-name {
    font-size: 250px; font-weight: 700;
    color: var(--ink); line-height: 1;
    writing-mode: vertical-rl;
    text-orientation: upright;
  }
  .brand-mark {
    width: 90px; height: 90px;
    background: var(--stamp);
    align-self: flex-end;
  }
</style>
</head>
<body>
  <main class="banner">
    <p class="copy copy-lead">瀬戸のブランド真鯛と選び抜いたワインで</p>
    <h1 class="copy copy-main">最高の贅沢を愉しむ</h1>
    <p class="copy copy-sub">神楽坂で味わう、&#12288;瀬戸の恵み</p>

    <div class="photo-fish" role="img" aria-label="竹ざるに盛られた真鯛二尾と枡に入った塩"></div>
    <div class="photo-wine" role="img" aria-label="白ワインが注がれたワイングラス"></div>

    <div class="brand">
      <span class="brand-name">汐凪</span>
      <span class="brand-mark" aria-hidden="true"></span>
    </div>
  </main>
</body>
</html>
```